Design business card using existing logo.

PLEASE DO NOT USE "RED WHITE & BLACK" color combo! Thank you.

Try different color combos such as:
- Vintage colors like brown, orange, gold, blue (not all together but a combo of 1 or 3
- Blue, w/ grey, or silver or white, Blue monochromatic can work as well.
- Use monochromatic variations on back (just an idea)

- Include full name, "Quillmark Records" on at least one side.

Target Market(s)

Teens

Industry/Entity Type

Business

Colors
3277b5
ffc214
f04a50
f78f20

```html
<!DOCTYPE html>
<html lang="en">
<head>
<meta charset="utf-8">
<title>Quillmark Records – Business Card</title>
<link rel="stylesheet" href="https://fonts.googleapis.com/css2?family=Open+Sans:wght@400;600;700&family=Montserrat:wght@500&display=swap">
<style>
  :root {
    --page-bg: #e9e6e3;
    --brand-blue: #3277b5;
    --brand-slate: #3d4a57;
    --brand-gold: #ffc214;
    --card-white: #ffffff;
    --ink: #3d4a57;
  }
  html, body {
    margin: 0;
    padding: 0;
    width: 1200px;
    height: 900px;
    overflow: hidden;
    background: var(--page-bg);
    font-family: "Open Sans", Arial, sans-serif;
  }
  .canvas {
    position: relative;
    width: 1200px;
    height: 900px;
  }
  .card {
    position: absolute;
    overflow: hidden;
    box-shadow: 0 6px 18px rgba(0,0,0,0.18);
  }
  /* Front */
  .card-front {
    left: 77px;
    top: 35px;
    width: 588px;
    height: 362px;
    background: var(--brand-blue);
    color: var(--card-white);
  }
  .front-art {
    position: absolute;
    inset: 0;
  }
  .holder {
    position: absolute;
    left: 31px;
    top: 36px;
  }
  .holder-name {
    margin: 0;
    font-weight: 700;
    font-size: 19px;
    letter-spacing: 0.2px;
    line-height: 1.2;
  }
  .holder-role {
    margin: 0;
    font-size: 15px;
    line-height: 1.3;
  }
  .contact-list {
    position: absolute;
    left: 31px;
    top: 195px;
    margin: 0;
    padding: 0;
    list-style: none;
    font-size: 15px;
    line-height: 22px;
  }
  .contact-list li {
    display: flex;
    align-items: center;
    gap: 8px;
  }
  .contact-list svg {
    width: 11px;
    height: 11px;
    fill: var(--card-white);
    flex: none;
  }
  .address {
    position: absolute;
    left: 31px;
    top: 284px;
    margin: 0;
    font-style: normal;
    font-size: 15px;
    line-height: 22px;
  }
  /* Back */
  .card-back {
    left: 388px;
    top: 505px;
    width: 567px;
    height: 352px;
    background: var(--card-white);
    text-align: center;
  }
  .brand-dot {
    position: absolute;
    left: 208px;
    top: 60px;
    width: 150px;
    height: 150px;
    border-radius: 50%;
    background: var(--brand-blue);
  }
  .brand-name {
    position: absolute;
    left: 0;
    right: 0;
    top: 232px;
    margin: 0;
    font-family: "Montserrat", Arial, sans-serif;
    font-weight: 500;
    font-size: 34px;
    line-height: 42px;
    letter-spacing: 1px;
    color: var(--brand-slate);
    white-space: nowrap;
  }
  .web-address {
    position: absolute;
    left: 0;
    right: 0;
    top: 294px;
    margin: 0;
    font-size: 17px;
    font-weight: 600;
    color: var(--ink);
  }
  .web-address .accent { color: var(--brand-blue); }
</style>
</head>
<body>
<main class="canvas">
  <section class="card card-front">
    <svg class="front-art" width="588" height="362" viewBox="0 0 588 362" aria-hidden="true">
      <rect x="300" y="0" width="288" height="362" fill="var(--card-white)"/>
      <circle cx="408" cy="180" r="180" fill="var(--brand-slate)"/>
      <circle cx="408" cy="180" r="150" fill="none" stroke="var(--brand-gold)" stroke-width="6"/>
    </svg>
    <div class="holder">
      <h1 class="holder-name">MARCUS HALE</h1>
      <p class="holder-role">Managing Director</p>
    </div>
    <ul class="contact-list">
      <li><svg viewBox="0 0 24 24"><path d="M6.6 10.8a15 15 0 0 0 6.6 6.6l2.2-2.2a1 1 0 0 1 1-.25 11.4 11.4 0 0 0 3.6.57 1 1 0 0 1 1 1V20a1 1 0 0 1-1 1A17 17 0 0 1 3 4a1 1 0 0 1 1-1h3.5a1 1 0 0 1 1 1c0 1.25.2 2.45.57 3.57a1 1 0 0 1-.25 1z"/></svg>(044)987650321</li>
      <li><svg viewBox="0 0 24 24"><rect x="1" y="4" width="22" height="16"/><path d="M2 5l10 8 10-8" stroke="var(--brand-blue)" stroke-width="2.5" fill="none"/></svg>hello@quillmark.com</li>
      <li><svg viewBox="0 0 24 24"><circle cx="12" cy="12" r="11"/></svg>www.quillmarkrec.com</li>
    </ul>
    <address class="address">5820, Harbor Lane Road,<br>Westbury, 40718</address>
  </section>

  <section class="card card-back">
    <div class="brand-dot" aria-hidden="true"></div>
    <h2 class="brand-name">QUILLMARK RECORDS</h2>
    <p class="web-address">www.<span class="accent">quillmark</span>.com</p>
  </section>
</main>
</body>
</html>
```